Flyer Erste-Hilfe-Kurse für Kinder
Zielgruppe
Wir sind eine private Firma und bieten verschiedene Erste-Hilfe-Kurse an.
Liebe Designer,
wir, die märkische Helferakademie, wollen uns im Bereich der Erste-Hilfe-Kurse für Kinder im Alter zwischen 6 bis 14 Jahre etablieren und wünschen uns daher einen passenden Flyer.
Folgende Sachen sind uns dabei besonders wichtig:
Märkische Helferakademie
Lindauer Weg 4
21079 Hamburg
Tel.: 040 71 84 29 03
Website: www.maerkische-helferakademie.de
In diesen Kursen lernen Kinder auf spielerische Art und Weise, Notfälle zu erkennen, sich zu organisieren und selbstständig Erste Hilfe zu leisten, auf Eigenschutz zu achten und einen Notruf abgeben zu können.
Weitere mögliche Themen sind: Auffinden einer bewusstlosen Person, Reanimation und Verbände.
Der Flyer soll farbenfroh gestaltet werden und darf gerne Bilder beinhalten.
Um einen Überblick über unsere Firma zu bekommen, kann man sich gerne unsere Website anschauen.
Der Flyer soll eine Vorder- und Rückseite haben.
Unser Logo kann für die Gestaltung von der Website genutzt werden und nach Auswahl des Gewinners von uns als Datei gerne bereitgestellt werden.
Wir freuen uns über Vorschläge.

```html
<!DOCTYPE html>
<html lang="de">
<head>
<meta charset="utf-8">
<title>Erste Hilfe für Kinder – Flyer</title>
<link rel="stylesheet" href="https://fonts.googleapis.com/css2?family=Fredoka:wght@500;600;700&family=Lilita+One&family=Patrick+Hand&family=Barlow+Condensed:wght@400;500;600;700&display=swap">
<style>
:root{
  --yellow:#fdd20a;
  --green:#8dc63f;
  --green-dark:#4fa83a;
  --purple:#6a2fa0;
  --purple-title:#5b2a93;
  --orange:#f7941d;
  --red:#e42434;
  --pink:#e5194b;
  --blue:#1b75d0;
  --sky:#dff0f8;
  --cream:#fdf8e6;
  --ink:#2a2a2a;
  --white:#ffffff;
  --stage:#eceef4;
}
*{box-sizing:border-box;margin:0;padding:0}
html,body{width:738px;height:1200px;overflow:hidden;background:var(--stage)}
body{position:relative;font-family:"Barlow Condensed",sans-serif;color:var(--ink)}
.page{position:absolute;left:164px;width:410px;height:570px;border-radius:10px;overflow:hidden;box-shadow:0 3px 10px rgba(0,0,0,.15)}
.page--front{top:20px;background:var(--yellow)}
.page--back{top:610px;background:var(--sky)}
.abs{position:absolute}
.layer{position:absolute;left:0;top:0}

/* front */
.brand{left:14px;top:14px;height:50px;padding:0 18px 0 12px;background:var(--white);border-radius:25px;display:flex;align-items:center;gap:8px;font-family:"Fredoka",sans-serif;font-weight:600;font-size:15px;line-height:1.05;color:var(--red)}
.brand__dot{width:14px;height:14px;border-radius:50%;background:var(--red);flex:none}
.kit{border-radius:10px;background:linear-gradient(160deg,#ff4a4a,#c8141e)}
.title{left:0;width:410px;top:72px;text-align:center;font-family:"Fredoka",sans-serif;font-weight:700;line-height:.92;letter-spacing:-.5px;-webkit-text-stroke:2px #fff;paint-order:stroke fill;text-shadow:2px 3px 0 rgba(0,0,0,.15)}
.title__l1{display:block;font-size:52px;color:var(--purple-title);transform:rotate(-2deg)}
.title__l2{display:block;font-size:56px;color:var(--green-dark);transform:rotate(-2deg)}
.title__l2 span{color:var(--orange)}
.ribbon{left:105px;top:177px;width:210px;height:30px;background:var(--red);color:var(--white);font-family:"Patrick Hand",cursive;font-size:19px;display:flex;align-items:center;justify-content:center;transform:rotate(-3deg);border-radius:2px}
.photo{left:150px;top:210px;width:260px;height:220px;border-radius:90px 0 0 0;background:linear-gradient(135deg,#a9d66a 0%,#f1d6c1 40%,#ffffff 70%,#e8eef0 100%)}
.bubble{left:14px;top:240px;width:124px;height:80px;background:var(--blue);border-radius:45% 50% 48% 40%;color:var(--white);font-family:"Patrick Hand",cursive;font-size:15px;line-height:1.1;display:flex;align-items:center;justify-content:center;text-align:center;transform:rotate(-4deg)}
.age{left:8px;top:330px;width:102px;height:102px;border-radius:50%;background:var(--purple);border:2px dashed rgba(255,255,255,.6);outline:4px solid var(--purple);color:var(--white);font-family:"Patrick Hand",cursive;text-align:center;font-size:15px;line-height:1;display:flex;flex-direction:column;justify-content:center;z-index:3}
.age strong{font-family:"Fredoka",sans-serif;font-size:24px;color:var(--yellow);font-weight:700;line-height:1.1}
.skills{left:12px;right:12px;top:448px;display:flex;z-index:3}
.skill{flex:1;text-align:center;color:var(--white);border-left:1px dashed rgba(255,255,255,.5)}
.skill:first-child{border-left:none}
.skill__icon{width:56px;height:56px;border-radius:50%;border:3px solid var(--white);margin:0 auto 6px;display:flex;align-items:center;justify-content:center}
.skill__name{font-family:"Barlow Condensed",sans-serif;font-weight:700;font-size:15px;letter-spacing:.3px}
.skill__text{font-size:10.5px;line-height:1.15;opacity:.95}

/* back */
.hero-boy{left:14px;top:14px;width:86px;height:112px;border-radius:40px 40px 10px 10px;background:linear-gradient(180deg,#8a5a33 0%,#f4c9a3 45%,#6cc04a 100%);opacity:.9}
.headline{left:100px;width:230px;top:16px;text-align:center;font-family:"Lilita One",sans-serif;line-height:1}
.headline__l1{display:block;font-size:25px;color:var(--white)}
.headline__l2{display:block;font-size:28px;color:var(--yellow)}
.headline__l3{display:inline-block;margin-top:5px;background:var(--purple);color:var(--white);font-size:21px;padding:3px 12px;transform:rotate(-2deg)}
.hero-kit{left:330px;top:40px;width:68px;height:80px;border-radius:10px;background:linear-gradient(160deg,#ff4a4a 0%,#c8141e 60%,#f0b37a 100%)}
.pill{font-family:"Lilita One",sans-serif;color:var(--white);font-size:13px;padding:3px 10px;border-radius:10px;letter-spacing:.3px}
.pill--blue{left:135px;top:140px;background:#1aa0df;z-index:2}
.pill--purple{left:12px;top:310px;background:var(--purple);transform:rotate(-2deg)}
.expect{left:10px;right:10px;top:152px;height:148px;background:var(--cream);border-radius:12px;border:3px solid #fff;display:flex;padding:8px 2px 4px}
.expect__col{flex:1;text-align:center;border-left:1px dotted #c9b98c;padding:0 2px}
.expect__col:first-child{border-left:none}
.expect__icon{width:40px;height:40px;border-radius:50%;margin:0 auto 5px;display:flex;align-items:center;justify-content:center;border:2px solid #fff;box-shadow:0 1px 2px rgba(0,0,0,.2)}
.expect__name{font-weight:700;font-size:11.5px;line-height:1.05;margin-bottom:4px}
.expect__text{font-size:9px;line-height:1.2;color:#333}
.topics{left:12px;top:328px;display:flex;gap:3px}
.topic{width:82px;height:132px;border-radius:4px;padding:5px 3px;text-align:center;display:flex;flex-direction:column;align-items:center}
.topic--yellow{background:#fde24f}
.topic--blue{background:#8ecbee}
.topic--green{background:#b9dc7c}
.topic__art{width:74px;height:56px;border-radius:6px;margin-bottom:6px}
.topic__name{font-weight:700;font-size:11px;line-height:1.05;margin-bottom:3px}
.topic__text{font-size:8.5px;line-height:1.2}
.burst{left:300px;top:345px;width:96px;height:80px;background:var(--yellow);clip-path:polygon(50% 0,60% 10%,75% 3%,80% 16%,96% 15%,92% 32%,100% 45%,92% 58%,98% 75%,82% 80%,78% 96%,62% 90%,50% 100%,38% 90%,22% 96%,18% 80%,2% 75%,8% 58%,0 45%,8% 32%,4% 15%,20% 16%,25% 3%,40% 10%);display:flex;align-items:center;justify-content:center;text-align:center;font-family:"Patrick Hand",cursive;font-size:13.5px;line-height:1.05;color:var(--purple-title);transform:rotate(-6deg)}
.footer{left:0;top:468px;width:410px;height:102px}
.contact{left:14px;top:508px;display:flex;gap:10px;z-index:2;color:var(--white)}
.contact__item{display:flex;gap:5px;font-size:10px;line-height:1.25;padding-right:10px;border-right:1px dashed rgba(255,255,255,.6)}
.contact__item:last-child{border-right:none}
.contact__item b{font-weight:600}
.ambulance{left:312px;top:448px;width:88px;height:68px;border-radius:12px 22px 8px 8px;background:linear-gradient(180deg,#ffffff 0%,#ffffff 55%,#e42434 56%,#e42434 70%,#ffffff 71%);box-shadow:0 2px 4px rgba(0,0,0,.25);z-index:2}
</style>
</head>
<body>

<!-- Front page -->
<section class="page page--front">
  <svg class="layer" width="410" height="570" viewBox="0 0 410 570" aria-hidden="true">
    <path d="M0,210 C90,188 200,222 410,192 L410,440 L0,440 Z" fill="var(--green)"/>
  </svg>
  <div class="abs brand"><span class="brand__dot"></span><span>Märkische<br>Helferakademie</span></div>
  <div class="abs kit" style="left:302px;top:16px;width:78px;height:58px" role="img" aria-label="Illustration eines roten Erste-Hilfe-Koffers"></div>
  <h1 class="abs title"><span class="title__l1">ERSTE HILFE</span><span class="title__l2">FÜR <span>KINDER</span></span></h1>
  <div class="abs ribbon">Spielend helfen lernen!</div>
  <div class="abs photo" role="img" aria-label="Foto: Mädchen legt einem Jungen im Arztkittel einen Kopfverband an"></div>
  <div class="abs bubble">Lerne, wie du<br>im Notfall richtig<br>handelst!</div>
  <svg class="layer" style="z-index:2" width="410" height="570" viewBox="0 0 410 570" aria-hidden="true">
    <path d="M0,425 C120,405 260,445 410,418 L410,570 L0,570 Z" fill="var(--purple)"/>
    <path d="M100,438 C200,430 300,450 410,430" fill="none" stroke="rgba(255,255,255,.5)" stroke-width="1.2" stroke-dasharray="5 4"/>
  </svg>
  <div class="abs age"><span>Für Kinder<br>von</span><strong>6 bis 14</strong><span>Jahren</span></div>
  <div class="abs skills">
    <div class="skill">
      <div class="skill__icon" style="background:#4ea83a">
        <svg width="30" height="30" viewBox="0 0 24 24" fill="none" stroke="#fff" stroke-width="1.8" stroke-linecap="round"><path d="M12 3a6 6 0 0 0-3.5 10.9V17h7v-3.1A6 6 0 0 0 12 3z"/><path d="M9.5 20h5"/></svg>
      </div>
      <div class="skill__name">VERSTEHEN</div>
      <div class="skill__text">Notfälle erkennen<br>und richtig handeln</div>
    </div>
    <div class="skill">
      <div class="skill__icon" style="background:var(--pink)">
        <svg width="30" height="30" viewBox="0 0 24 24" fill="none" stroke="#fff" stroke-width="2.4"><path d="M12 20s-7-4.4-7-10a4 4 0 0 1 7-2.6A4 4 0 0 1 19 10c0 5.6-7 10-7 10z"/></svg>
      </div>
      <div class="skill__name">HELFEN</div>
      <div class="skill__text">Erste Hilfe<br>leisten können</div>
    </div>
    <div class="skill">
      <div class="skill__icon" style="background:var(--blue)">
        <svg width="30" height="30" viewBox="0 0 24 24" fill="none" stroke="#fff" stroke-width="2.2"><path d="M12 3l7 3v5c0 5-3 8-7 10-4-2-7-5-7-10V6z"/></svg>
      </div>
      <div class="skill__name">SCHÜTZEN</div>
      <div class="skill__text">Auf Eigenschutz<br>achten</div>
    </div>
    <div class="skill">
      <div class="skill__icon" style="background:var(--orange)">
        <svg width="30" height="30" viewBox="0 0 24 24" fill="#fff"><path d="M6.6 10.8a15 15 0 0 0 6.6 6.6l2.2-2.2c.3-.3.7-.4 1-.2 1.1.4 2.3.6 3.6.6.6 0 1 .4 1 1V20c0 .6-.4 1-1 1A17 17 0 0 1 3 4c0-.6.4-1 1-1h3.5c.6 0 1 .4 1 1 0 1.3.2 2.5.6 3.6.1.3 0 .7-.2 1z"/></svg>
      </div>
      <div class="skill__name">NOTRUF</div>
      <div class="skill__text">Einen Notruf<br>richtig absetzen</div>
    </div>
  </div>
</section>

<!-- Back page -->
<section class="page page--back">
  <svg class="layer" width="410" height="570" viewBox="0 0 410 570" aria-hidden="true">
    <path d="M0,0 H410 V125 C300,138 150,120 0,135 Z" fill="#6cb33f"/>
  </svg>
  <div class="abs hero-boy" role="img" aria-label="Illustration eines Comic-Jungen mit Daumen hoch"></div>
  <h2 class="abs headline"><span class="headline__l1">WIR MACHEN</span><span class="headline__l2">KINDER STARK</span><span class="headline__l3">FÜRS LEBEN!</span></h2>
  <div class="abs hero-kit" role="img" aria-label="Illustration eines Erste-Hilfe-Koffers mit Pflaster"></div>

  <div class="abs pill pill--blue">DAS ERWARTET EUCH:</div>
  <div class="abs expect">
    <div class="expect__col">
      <div class="expect__icon" style="background:#3aa935">
        <svg width="22" height="22" viewBox="0 0 24 24" fill="none" stroke="#fff" stroke-width="2.2" stroke-linejoin="round"><path d="M12 3L2 20h20z"/><path d="M12 10v5M12 17.5v.5"/></svg>
      </div>
      <div class="expect__name" style="color:#3aa935">NOTFÄLLE<br>ERKENNEN</div>
      <div class="expect__text">Gefahren erkennen<br>und richtig<br>reagieren</div>
    </div>
    <div class="expect__col">
      <div class="expect__icon" style="background:var(--pink)">
        <svg width="22" height="22" viewBox="0 0 24 24" fill="#fff"><path d="M6.6 10.8a15 15 0 0 0 6.6 6.6l2.2-2.2c.3-.3.7-.4 1-.2 1.1.4 2.3.6 3.6.6.6 0 1 .4 1 1V20c0 .6-.4 1-1 1A17 17 0 0 1 3 4c0-.6.4-1 1-1h3.5c.6 0 1 .4 1 1 0 1.3.2 2.5.6 3.6.1.3 0 .7-.2 1z"/></svg>
      </div>
      <div class="expect__name" style="color:var(--pink)">NOTRUF<br>ABSETZEN</div>
      <div class="expect__text">Einen Notruf<br>richtig absetzen<br>und wichtige<br>Infos durchgeben</div>
    </div>
    <div class="expect__col">
      <div class="expect__icon" style="background:var(--blue)">
        <svg width="22" height="22" viewBox="0 0 24 24" fill="#fff"><path d="M12 14s-5-3-5-6.5A2.7 2.7 0 0 1 12 6a2.7 2.7 0 0 1 5 1.5C17 11 12 14 12 14z"/><path d="M3 17h5l3 2h7l3-3" fill="none" stroke="#fff" stroke-width="1.8"/></svg>
      </div>
      <div class="expect__name" style="color:var(--blue)">ERSTE HILFE<br>LEISTEN</div>
      <div class="expect__text">Auf spielerische<br>Weise Erste Hilfe<br>leisten lernen</div>
    </div>
    <div class="expect__col">
      <div class="expect__icon" style="background:var(--orange)">
        <svg width="22" height="22" viewBox="0 0 24 24" fill="none" stroke="#fff" stroke-width="2.2"><path d="M12 3l7 3v5c0 5-3 8-7 10-4-2-7-5-7-10V6z"/></svg>
      </div>
      <div class="expect__name" style="color:var(--orange)">EIGENSCHUTZ<br>BEACHTEN</div>
      <div class="expect__text">Sich selbst schützen<br>und sicher<br>handeln</div>
    </div>
    <div class="expect__col">
      <div class="expect__icon" style="background:#7e3fa8">
        <svg width="22" height="22" viewBox="0 0 24 24" fill="none" stroke="#fff" stroke-width="2" stroke-linecap="round"><circle cx="12" cy="6" r="2.5"/><path d="M12 9v5M6 12l6 2 6-2M5 19c3-2 11-2 14 0"/></svg>
      </div>
      <div class="expect__name" style="color:#7e3fa8">RUHIG<br>BLEIBEN</div>
      <div class="expect__text">Ruhig bleiben,<br>überlegen und<br>sich organisieren</div>
    </div>
  </div>

  <div class="abs pill pill--purple">WEITERE SPANNENDE THEMEN:</div>
  <div class="abs topics">
    <div class="topic topic--yellow">
      <div class="topic__art" style="background:linear-gradient(135deg,#7cc24a,#f3c9a0 55%,#3a8fd0)" role="img" aria-label="Illustration: Kinder finden eine am Boden liegende Person"></div>
      <div class="topic__name" style="color:var(--purple-title)">AUFFINDEN EINER<br>BEWUSSTLOSEN PERSON</div>
      <div class="topic__text">Was tun, wenn jemand<br>nicht reagiert?</div>
    </div>
    <div class="topic topic--blue">
      <div class="topic__art" style="display:flex;align-items:center;justify-content:center">
        <svg width="48" height="44" viewBox="0 0 24 22"><path d="M12 21S2 14.6 2 7.5A5 5 0 0 1 12 4.5a5 5 0 0 1 10 3C22 14.6 12 21 12 21z" fill="#e42434" stroke="#fff" stroke-width="1"/><path d="M4 10h4l1.5-3 2.5 6 2-4 1 1h5" fill="none" stroke="#fff" stroke-width="1.2"/></svg>
      </div>
      <div class="topic__name" style="color:#1a5fa8">REANIMATION</div>
      <div class="topic__text">Herzdruckmassage<br>kindgerecht erklärt<br>und geübt</div>
    </div>
    <div class="topic topic--green">
      <div class="topic__art" style="background:linear-gradient(135deg,#ffffff,#e8d9c2 50%,#f0b37a)" role="img" aria-label="Illustration: Verbandrolle und Pflaster"></div>
      <div class="topic__name" style="color:#2f7d24">VERBÄNDE</div>
      <div class="topic__text">Pflaster und<br>Verbände anlegen –<br>ganz praktisch!</div>
    </div>
  </div>
  <div class="abs burst">Mitmachen &amp;<br>Sicherheit<br>gewinnen!</div>

  <svg class="abs footer" width="410" height="102" viewBox="0 0 410 102" aria-hidden="true">
    <path d="M0,18 C130,8 280,24 410,6 V102 H0 Z" fill="var(--red)"/>
    <path d="M8,30 C130,20 280,34 402,18" fill="none" stroke="#fff" stroke-width="1" stroke-dasharray="5 4"/>
  </svg>
  <div class="abs ambulance" role="img" aria-label="Illustration eines Krankenwagens"></div>
  <div class="abs contact">
    <div class="contact__item">
      <svg width="11" height="14" viewBox="0 0 24 30" fill="#fff"><path d="M12 0a10 10 0 0 0-10 10c0 7.5 10 20 10 20s10-12.5 10-20A10 10 0 0 0 12 0zm0 14a4 4 0 1 1 0-8 4 4 0 0 1 0 8z"/></svg>
      <div><b>Märkische Helferakademie</b><br>Lindauer Weg 4<br>21079 Hamburg</div>
    </div>
    <div class="contact__item">
      <svg width="12" height="12" viewBox="0 0 24 24" fill="#fff"><path d="M6.6 10.8a15 15 0 0 0 6.6 6.6l2.2-2.2c.3-.3.7-.4 1-.2 1.1.4 2.3.6 3.6.6.6 0 1 .4 1 1V20c0 .6-.4 1-1 1A17 17 0 0 1 3 4c0-.6.4-1 1-1h3.5c.6 0 1 .4 1 1 0 1.3.2 2.5.6 3.6.1.3 0 .7-.2 1z"/></svg>
      <div>Tel.:<br>040 71 84 29 03</div>
    </div>
    <div class="contact__item">
      <svg width="12" height="12" viewBox="0 0 24 24" fill="none" stroke="#fff" stroke-width="2"><circle cx="12" cy="12" r="10"/><path d="M2 12h20M12 2c3 3 3 17 0 20M12 2c-3 3-3 17 0 20"/></svg>
      <div>www.maerkische-<br>helferakademie.de</div>
    </div>
  </div>
</section>

</body>
</html>
```